New wine label design aimed at millennials

We have developed 2 new quality wines - a crisp, cool climate Chardonnay from the Orange region and a spicy Shiraz from the Gundagai wine region.

Each of these wines have been made in a distinctly modern style, with less oak and more elegance than most and come from two relatively new but exciting wine regions.

They are distinctly food friendly as a result.

These are classic varieties, with a modern take from 'undiscovered' regions.

We are seeking to target millennial wine drinkers who are possibly new to wine or are early in their journey into wine.

We are after a contemporary single label design (i.e. - not a font ab back label) to be applied to a 'lean green' burgundy bottle that speaks to the modern take on classic varieties from undiscovered regions.

We have already recieved a umber of good designs based on some possible brand names:

Tessaly
Copper and Quill
The Velvet Almanac

And now we would like to purse labels focusing just on Copper and Quill (of course if a bolt of lightening strikes you on the other names, feel free!)

the reference to Copper and Quill comes from a story attached to one of our existing labels – Marion Treloar. The two Treloar brothers who founded this Vineyard famously borrowed a Copper and Quill from a well-established winery family in order for them to roam the local foothills in order to find their ideal vineyard site.

We would like to capture this sense of exploration and discovery in what would form a sub-tier label for this brand.

It would still be targeting very much millennial's and so we want the label to look contemporary and urban, but reflect the sense of exploration and discovery awhile referencing the historical authenticity of the whole overarching brand structure.

I have attached a number of inspirational images that would need to be translated into a more modern visual setting.

obviously use of a horse and a matter in some sort of "branded" image would be a first step and obviously the historical/authentic back story combined with a modern anaesthetic lends itself to plain black-and-white.

However, clever use of a modern colour palette would also be very welcome.
Updates

For further inspiration we have been considering the following phrases and words as possible label namesGallivant - giving a sense of freewheeling adventure and explorationHorse & Mattock - referencing an old story of 2 pioneer vignerons being lent a horse and a mattock to go out and find their ideal vineyard sites, introducing concepts of innovation, discovery and authenticityThe Gentleman Vigneron - referencing a founding winemakers nominal descriptor of himself and bringing a true element of authenticity and quality. Added Monday, July 31, 2017

Project Deadline Extended Reason: I am hoping to give some more information and focus on the desired outcomes.The name of the label will be Copper and Quill.Please review the prior comments to get the background on this and I will add more information as well.I will try to identify and provide some other design work that aligns with what we are trying to achieve also. Added Friday, August 11, 2017

Target Market(s)

Millennials, skewing female 21-35 years, university educated, employed in white collar or professional industry, urban

Font styles to use
Serif
Sans Serif

Colors

Designer to choose colors to be used in the design.

Requirements
Must have
• Modern, contemporary urban look and feel that stands out on the shelf.
• Must be relevant and attractive to millennials.
• Sense of humour or quirkiness to it.
• We like this label amongst many other
• http://www.pellbrookcellars.com/shopwines/
Nice to have
• We will aim to use recycled/low carbon footprint glass in the packaging (i.e. the lean green bottles) so would also aim to use 100% recycled paper on the label and would like to mention this in the design.

```html
<!DOCTYPE html>
<html lang="en">
<head>
<meta charset="utf-8">
<title>Copper &amp; Quill wine labels</title>
<link rel="stylesheet" href="https://fonts.googleapis.com/css2?family=Raleway:wght@300;400&display=swap">
<style>
  :root {
    --page: #ffffff;
    --chard-bg: #5c5e55;
    --chard-ink: #c3c43f;
    --shiraz-bg: #cdd6c9;
    --shiraz-ink: #5e1014;
  }
  * { margin: 0; padding: 0; box-sizing: border-box; }
  html, body { width: 1200px; height: 726px; overflow: hidden; background: var(--page); }
  body { position: relative; font-family: "Raleway", sans-serif; font-weight: 300; }

  .label {
    position: absolute; top: 51px; width: 352px; height: 618px; overflow: hidden;
    background: var(--bg); color: var(--ink);
  }
  .label--chardonnay { left: 22px; --bg: var(--chard-bg); --ink: var(--chard-ink); }
  .label--shiraz { left: 392px; --bg: var(--shiraz-bg); --ink: var(--shiraz-ink); }

  .label > * { position: absolute; white-space: nowrap; }
  .rule-h { height: 2px; background: var(--ink); }
  .rule-v { width: 2px; background: var(--ink); }
  .rule-dash { width: 0; border-left: 2px dashed var(--ink); }

  .brand-seal {
    left: 25px; top: 12px; width: 122px; height: 122px;
    border: 2px solid var(--ink); border-radius: 50%;
    display: flex; align-items: center; justify-content: center;
    text-align: center; font-size: 17px; line-height: 1.15; letter-spacing: 0.5px;
  }

  .abv { left: 194px; top: 8px; font-size: 98px; line-height: 1; letter-spacing: -5px; }
  .abv-note { left: 185px; top: 114px; font-size: 18.5px; line-height: 1; letter-spacing: -0.2px; }

  .variety { left: 0; width: 100%; text-align: center; line-height: 1; font-weight: 300; }
  .label--chardonnay .variety { top: 152px; font-size: 60px; }
  .label--shiraz .variety { top: 146px; font-size: 70px; }

  .region-map { left: 12px; top: 246px; width: 210px; height: 192px; border-radius: 40px 60px 30px 50px; background: var(--ink); opacity: 0.9; }
  .region-name { right: 16px; top: 264px; text-align: right; font-size: 26px; line-height: 0.98; }
  .pin-line { border-top: 2px solid var(--ink); border-left: 2px solid var(--ink); }
  .pin-dot { width: 8px; height: 8px; border-radius: 50%; background: var(--bg); border: 2px solid var(--ink); }

  .tasting { left: 12px; text-transform: uppercase; line-height: 0.83; }
  .tasting--cool { top: 462px; font-size: 52px; letter-spacing: -1.5px; }
  .tasting--slightly { top: 468px; font-size: 46px; letter-spacing: -1px; line-height: 1; }
  .tasting--sweet { top: 508px; font-size: 64px; letter-spacing: -1.5px; line-height: 1; }

  .note-vertical {
    left: 242px; top: 350px; width: 90px; height: 218px;
    writing-mode: vertical-rl; transform: rotate(180deg);
    font-size: 62px; line-height: 90px; text-align: left; text-transform: uppercase; letter-spacing: 1px;
  }
  .eco { left: 0; top: 582px; width: 100%; text-align: center; font-size: 24px; line-height: 1; letter-spacing: -0.5px; }
</style>
</head>
<body>

<section class="label label--chardonnay" aria-label="Chardonnay label">
  <div class="brand-seal">copper<br>&amp; quill</div>
  <div class="rule-dash" style="left:178px; top:6px; height:135px;"></div>
  <div class="abv">14%</div>
  <div class="abv-note">alcohol by volume</div>
  <div class="rule-h" style="left:0; top:144px; width:352px;"></div>
  <h2 class="variety">chardonnay</h2>
  <div class="rule-h" style="left:0; top:224px; width:352px;"></div>

  <div class="region-map" role="img" aria-label="Map of Australia marking the Orange region"></div>
  <p class="region-name">orange<br>region</p>
  <div class="pin-line" style="left:190px; top:297px; width:52px; height:66px;"></div>
  <div class="pin-dot" style="left:186px; top:360px;"></div>

  <div class="rule-h" style="left:12px; top:448px; width:210px;"></div>
  <div class="rule-v" style="left:234px; top:349px; height:220px;"></div>
  <div class="rule-v" style="left:338px; top:349px; height:220px;"></div>
  <p class="tasting tasting--cool">Cool-<br>Climate</p>
  <p class="note-vertical">Crisp</p>
  <div class="rule-h" style="left:12px; top:576px; width:328px; height:1px;"></div>
  <p class="eco">ECO-FRIENDLY PACKAGING</p>
</section>

<section class="label label--shiraz" aria-label="Shiraz label">
  <div class="brand-seal">copper<br>&amp; quill</div>
  <div class="rule-dash" style="left:174px; top:10px; height:135px;"></div>
  <div class="abv">14%</div>
  <div class="abv-note">alcohol by volume</div>
  <div class="rule-h" style="left:0; top:146px; width:352px;"></div>
  <h2 class="variety">shiraz</h2>
  <div class="rule-h" style="left:0; top:226px; width:352px;"></div>

  <div class="region-map" role="img" aria-label="Map of Australia marking the Gundagai region"></div>
  <p class="region-name" style="top:258px;">gundagai<br>region</p>
  <div class="pin-line" style="left:190px; top:297px; width:52px; height:66px;"></div>
  <div class="pin-dot" style="left:186px; top:360px;"></div>

  <div class="rule-h" style="left:12px; top:450px; width:210px;"></div>
  <div class="rule-v" style="left:234px; top:349px; height:220px;"></div>
  <div class="rule-v" style="left:338px; top:349px; height:220px;"></div>
  <p class="tasting tasting--slightly">Slightly</p>
  <p class="tasting tasting--sweet">Sweet</p>
  <p class="note-vertical">Spicy</p>
  <p class="eco">ECO-FRIENDLY PACKAGING</p>
</section>

</body>
</html>
```